Pediatric Pelvic Health Brochure

Looking to design a brochure for Marlow Brook's pelvic health program. I can provide imagery once I see the layout. Our website is marlowbrookpt.example so the look should reflect that

If you see PDF titled blue and word doc you will see what we provided as thoguhts.

Target Market(s)

parents of children

Industry/Entity Type

Health And Wellness

Font styles to use
Serif

Requirements
Must have
• clear call outs - easy to read with copy,
Should not have
• not look bland or dated

```html
<!DOCTYPE html>
<html lang="en">
<head>
<meta charset="utf-8">
<title>Marlow Brook – Pediatric Pelvic Health Brochure</title>
<link rel="stylesheet" href="https://fonts.googleapis.com/css2?family=PT+Serif:ital,wght@0,400;0,700;1,700&family=Montserrat:wght@400;500;600;700&display=swap">
<style>
  :root {
    --navy: #1f3891;
    --royal: #2a4fb4;
    --sky: #1ea8e0;
    --sky-light: #5cc3ee;
    --mist: #dcebf7;
    --paper: #ffffff;
    --ink: #27314d;
    --stage: #e4e5e8;
    --photo-a: #cfdbe6;
    --photo-b: #eef2f6;
  }
  * { box-sizing: border-box; margin: 0; padding: 0; }
  html, body { width: 1200px; height: 2400px; overflow: hidden; }
  body {
    background: var(--stage);
    font-family: "Montserrat", Arial, sans-serif;
    color: var(--ink);
    position: relative;
  }
  .spread {
    position: absolute;
    left: 50px;
    width: 1100px;
    height: 850px;
    display: grid;
    grid-template-columns: repeat(3, 1fr);
    background: var(--paper);
    box-shadow: 0 20px 40px rgba(40, 50, 70, .18);
  }
  .spread--outside { top: 230px; }
  .spread--inside { top: 1320px; }
  .panel { position: relative; overflow: hidden; }
  .panel + .panel { border-left: 1px solid rgba(31, 56, 145, .08); }
  .serif { font-family: "PT Serif", Georgia, serif; }

  .photo {
    background: linear-gradient(160deg, var(--photo-b), var(--photo-a));
  }

  /* ---------- Back panel: diagnoses ---------- */
  .panel--diagnoses { background: var(--mist); padding: 44px 32px 0; }
  .diagnoses__title {
    font-family: "PT Serif", Georgia, serif;
    font-style: italic;
    font-weight: 700;
    color: var(--navy);
    font-size: 26px;
    line-height: 1.15;
    text-transform: uppercase;
  }
  .diagnoses__list {
    margin-top: 26px;
    display: grid;
    grid-template-columns: 1fr 1fr;
    column-gap: 18px;
    row-gap: 12px;
    list-style: none;
    font-size: 11px;
    line-height: 1.3;
    color: var(--navy);
  }
  .diagnoses__list li { padding-left: 16px; position: relative; }
  .diagnoses__list li::before {
    content: "";
    position: absolute; left: 0; top: 2px;
    width: 9px; height: 9px;
    background: linear-gradient(90deg, var(--navy) 50%, var(--sky) 50%);
  }
  .diagnoses__photo {
    position: absolute; left: 0; right: 0; bottom: 0; height: 390px;
    background: linear-gradient(160deg, #e8f1f8, #b9cfe2);
  }

  /* ---------- Middle panel: contact ---------- */
  .panel--contact { background: var(--mist); padding: 22px 22px; }
  .contact__card {
    height: 100%;
    border-radius: 0 46px 0 46px;
    background: linear-gradient(180deg, var(--royal) 0%, #2573cc 50%, var(--sky) 100%);
    color: #fff;
    text-align: center;
    padding: 54px 26px 40px;
    display: flex; flex-direction: column; align-items: center;
  }
  .contact__offer {
    font-style: italic; font-weight: 600; font-size: 17px; line-height: 1.35;
  }
  .contact__cta {
    margin-top: 16px;
    background: var(--sky);
    border-radius: 14px;
    padding: 4px 20px;
    font-weight: 600; font-size: 13px; letter-spacing: .04em;
  }
  .contact__phone { margin-top: 10px; font-weight: 700; font-size: 34px; letter-spacing: .01em; }
  .brand {
    display: flex; align-items: center; gap: 12px;
  }
  .brand__mark { width: 38px; height: 38px; background: currentColor; flex: none; }
  .brand__text { text-align: left; }
  .brand__name { font-family: "PT Serif", Georgia, serif; font-size: 34px; line-height: 1; }
  .brand__tag { font-family: "PT Serif", Georgia, serif; font-size: 9.5px; letter-spacing: .08em; text-transform: uppercase; margin-top: 4px; }
  .contact__brand { margin-top: 100px; color: #fff; }
  .contact__icons { margin-top: 110px; display: flex; gap: 12px; }
  .contact__icons svg { width: 34px; height: 34px; }
  .contact__details { margin-top: 24px; font-size: 15px; font-weight: 500; line-height: 1.5; }
  .contact__details p + p { margin-top: 10px; }

  /* ---------- Front cover ---------- */
  .panel--cover { padding: 40px 30px; }
  .cover__brand { color: var(--navy); justify-content: center; }
  .cover__brand .brand__mark { background: var(--sky); }
  .cover__brand .brand__tag { color: var(--sky); }
  .cover__frame {
    position: absolute; left: 40px; right: 30px; top: 150px; height: 470px;
    border: 2px solid var(--navy);
    border-radius: 0 40px 0 0;
  }
  .cover__photo { position: absolute; left: 60px; right: 50px; top: 168px; height: 440px; }
  .cover__title {
    position: absolute; left: 30px; right: 60px; top: 530px;
    background: var(--sky);
    border-radius: 0 0 44px 0;
    color: #fff;
    padding: 24px 26px 26px;
  }
  .cover__title h1 {
    font-family: "PT Serif", Georgia, serif; font-weight: 700; font-size: 42px; line-height: 1; letter-spacing: .01em;
  }
  .cover__title h2 {
    font-family: "PT Serif", Georgia, serif; font-weight: 700; font-size: 27px; line-height: 1.1; margin-top: 4px;
  }
  .cover__title p { margin-top: 10px; font-size: 18px; line-height: 1.3; }
  .cover__web {
    position: absolute; left: 0; right: 0; bottom: 40px; text-align: center;
    color: var(--navy); font-weight: 600; font-size: 18px; letter-spacing: .12em;
  }

  /* ---------- Inside ---------- */
  .panel--help { padding: 50px 34px 0; }
  .section-title {
    font-family: "PT Serif", Georgia, serif; font-weight: 700; font-size: 22px;
    text-transform: uppercase; letter-spacing: .02em;
  }
  .panel--help .section-title { color: var(--navy); }
  .section-rule { width: 150px; height: 2px; background: var(--sky); margin: 6px 0 18px; }
  .copy { font-size: 12.5px; line-height: 1.5; }
  .copy p + p { margin-top: 12px; }
  .help__photo { position: absolute; left: 0; right: 0; bottom: 0; height: 330px; background: linear-gradient(160deg, #e6eef6, #b8cde0); }

  .inside-blue {
    grid-column: 2 / 4;
    position: relative;
    background: linear-gradient(135deg, var(--navy) 0%, var(--royal) 100%);
    color: #fff;
    display: grid;
    grid-template-columns: 1fr 1fr;
    grid-template-rows: 300px auto 1fr;
  }
  .team__photo {
    grid-column: 1 / 3;
    margin: 30px 30px 0;
    border-radius: 0 40px 0 40px;
    background: linear-gradient(160deg, #f0f3f7, #c7d3e0);
    border: 3px solid rgba(255,255,255,.5);
  }
  .service { padding: 30px 32px 0; }
  .service .section-rule { background: var(--sky-light); width: 120px; }
  .service .copy { font-size: 12.5px; color: #eaf2ff; }
  .reviews { grid-column: 1 / 3; position: relative; padding: 26px 32px 34px; }
  .reviews__band {
    background: var(--sky);
    margin: 0 -32px;
    padding: 8px 32px;
    font-family: "PT Serif", Georgia, serif; font-weight: 700;
    font-size: 20px; letter-spacing: .4em; text-transform: uppercase; text-align: center;
  }
  .reviews__grid { display: grid; grid-template-columns: 1fr 1fr; gap: 40px; margin-top: 22px; }
  .review {
    position: relative;
    border: 1px solid rgba(255,255,255,.35);
    border-radius: 0 28px 0 28px;
    padding: 22px 20px 16px;
    font-size: 11.5px; line-height: 1.5; color: #eaf2ff;
  }
  .review__mark {
    position: absolute; font-family: "PT Serif", Georgia, serif; font-size: 40px; line-height: 1; color: var(--sky-light);
  }
  .review__mark--open { top: -16px; left: 50%; transform: translateX(-50%); background: var(--royal); padding: 0 6px; }
  .review__mark--close { bottom: -26px; right: 40px; background: var(--royal); padding: 0 6px; }
  .review__name { text-align: right; color: var(--sky-light); font-size: 11px; margin-top: 4px; }
</style>
</head>
<body>

<!-- Outside of the tri-fold -->
<section class="spread spread--outside">
  <div class="panel panel--diagnoses">
    <h3 class="diagnoses__title">We treat a<br>range of diagnoses</h3>
    <ul class="diagnoses__list">
      <li>Constipation</li>
      <li>Waking up in the night to urinate or nocturia</li>
      <li>Increased urinary frequency</li>
      <li>Difficulty with urination: straining, slow flow, pain during or after urination</li>
      <li>Decreased urinary frequency</li>
      <li>Reduced sensation of bladder or bowel fullness</li>
      <li>Day-time incontinence</li>
      <li>Pain in the abdomen, bladder or lower back</li>
      <li>Night-time incontinence, bed-wetting or enuresis</li>
      <li>Fecal incontinence</li>
      <li>Giggle incontinence</li>
      <li>Treatment after pediatric pelvic surgeries</li>
      <li>Incontinence in the athletic female child or teenager</li>
    </ul>
    <div class="diagnoses__photo" role="img" aria-label="Photo of a smiling parent and young daughter talking with a physician holding a clipboard"></div>
  </div>

  <div class="panel panel--contact">
    <div class="contact__card">
      <p class="contact__offer">We offer a FREE 15 minute consultation to help you determine if therapy is right for you.</p>
      <span class="contact__cta">CALL US TODAY!</span>
      <p class="contact__phone">555.014.2600</p>
      <div class="brand contact__brand">
        <span class="brand__mark"></span>
        <div class="brand__text">
          <div class="brand__name">Marlow Brook</div>
          <div class="brand__tag">Physical and Aquatic Therapy</div>
        </div>
      </div>
      <div class="contact__icons">
        <svg viewBox="0 0 34 34" aria-hidden="true"><circle cx="17" cy="17" r="15.5" fill="none" stroke="#fff" stroke-width="2"/><rect x="9" y="11.5" width="16" height="11" rx="1.5" fill="none" stroke="#fff" stroke-width="1.8"/><path d="M9.5 12.5 17 18l7.5-5.5" fill="none" stroke="#fff" stroke-width="1.8"/></svg>
        <svg viewBox="0 0 34 34" aria-hidden="true"><circle cx="17" cy="17" r="15.5" fill="none" stroke="#fff" stroke-width="2"/><circle cx="17" cy="17" r="8" fill="none" stroke="#fff" stroke-width="1.6"/><ellipse cx="17" cy="17" rx="3.5" ry="8" fill="none" stroke="#fff" stroke-width="1.4"/><path d="M9 17h16" stroke="#fff" stroke-width="1.4"/></svg>
        <svg viewBox="0 0 34 34" aria-hidden="true"><circle cx="17" cy="17" r="15.5" fill="none" stroke="#fff" stroke-width="2"/><path d="M17 26s-6-6.5-6-11a6 6 0 0 1 12 0c0 4.5-6 11-6 11z" fill="none" stroke="#fff" stroke-width="1.8"/><circle cx="17" cy="15" r="2.2" fill="#fff"/></svg>
      </div>
      <div class="contact__details">
        <p>care@marlowbrookpt.example</p>
        <p>marlowbrookpt.example</p>
        <p>48 Linden Avenue<br>Ground Floor<br>Riverton, NY 10099</p>
      </div>
    </div>
  </div>

  <div class="panel panel--cover">
    <div class="brand cover__brand">
      <span class="brand__mark"></span>
      <div class="brand__text">
        <div class="brand__name">Marlow Brook</div>
        <div class="brand__tag">Physical and Aquatic Therapy</div>
      </div>
    </div>
    <div class="cover__frame"></div>
    <div class="cover__photo photo" role="img" aria-label="Portrait photo of a smiling female doctor in a white coat with a stethoscope"></div>
    <div class="cover__title">
      <h1>PEDIATRIC</h1>
      <h2>PELVIC HEALTH</h2>
      <p>Treating Infants,<br>Children &amp; Adolescents</p>
    </div>
    <p class="cover__web">www.marlowbrookpt.example</p>
  </div>
</section>

<!-- Inside of the tri-fold -->
<section class="spread spread--inside">
  <div class="panel panel--help">
    <h3 class="section-title">We Help</h3>
    <div class="section-rule"></div>
    <div class="copy">
      <p>Although millions of children suffer from pelvic floor dysfunction, it often takes a long time to receive the right treatment.</p>
      <p>Typically, children are toilet trained by age 4. After age 4, bowel and bladder dysfunction is considered a major medical issue that affects the family unit.</p>
      <p>Pelvic problems in children greatly influence the quality of life, self-image, social interactions, participation in sports, etc. A pelvic physical therapist can help restore normality in bladder and bowel function and prevent the progression of problems that, if untreated, may be carried over into adult life.</p>
    </div>
    <div class="help__photo" role="img" aria-label="Photo of a smiling doctor listening to a young girl's heartbeat with a stethoscope"></div>
  </div>

  <div class="inside-blue">
    <div class="team__photo" role="img" aria-label="Photo of the smiling clinical team in white coats and scrubs"></div>

    <div class="service">
      <h3 class="section-title">We Specialize</h3>
      <div class="section-rule"></div>
      <div class="copy">
        <p>All pelvic physical therapy treatments are always done with a physical therapist trained in pediatric pelvic floor issues, and always with your doctor's knowledge. Children are dressed and parents and guardians are present.</p>
        <p>During each session, your child or teen will work exclusively with one of our pelvic health physical therapists to help build strength, improve movement, and strengthen the skills and confidence needed to complete daily activities.</p>
      </div>
    </div>

    <div class="service">
      <h3 class="section-title">We Partner</h3>
      <div class="section-rule"></div>
      <div class="copy">
        <p>Pelvic dysfunction problems in children in general, and in those with neurological pathologies even more, are markedly different from those in adults. Thus a therapist needs to work with parents, teachers and other healthcare professionals such as urologists, GI's, pediatric physical therapists and psychologists to provide an integrated and comprehensive plan of care.</p>
      </div>
    </div>

    <div class="reviews">
      <h3 class="reviews__band">What our clients say</h3>
      <div class="reviews__grid">
        <blockquote class="review">
          <span class="review__mark review__mark--open">&ldquo;</span>
          After months of trying other options, I was so relieved we came to Marlow Brook Physical Therapy. Our son felt comfortable from the very first visit, and the home exercises were simple to follow. Within a few weeks his nights were dry and his confidence was back.
          <div class="review__name">- Dana R</div>
          <span class="review__mark review__mark--close">&rdquo;</span>
        </blockquote>
        <blockquote class="review">
          <span class="review__mark review__mark--open">&ldquo;</span>
          After months of trying other options, I was so relieved we came to Marlow Brook Physical Therapy. Our son felt comfortable from the very first visit, and the home exercises were simple to follow. Within a few weeks his nights were dry and his confidence was back.
          <div class="review__name">- Dana R</div>
          <span class="review__mark review__mark--close">&rdquo;</span>
        </blockquote>
      </div>
    </div>
  </div>
</section>

</body>
</html>
```